Rio Dorado Salsa – CPG Website with WordPress - Store Locator: WP Maps plugin

Larkmoor Food Company is a startup consumer packaged goods (CPG) brand launching its flagship product line — Rio Dorado Salsa. We’re seeking a talented web designer to create a bold, professional, mobile-optimized website using WordPress with a WP Maps store locator to help customers find local retailers.

Our goal is to build a strong online presence that supports both retail growth and direct-to-consumer sales.

See Rio Dorado _Website_Design_Brief word document.

The website URL is https://riodoradosalsa.example/

Target Market(s)

Consumers of gourmet salsa

Industry/Entity Type

Consumer Packaged Goods - Salsa manufacturer.

Coding

Coded - Design and coding required

Number of Pages Required

5+ page

Requirements
Must have
• The design of the Rio Dorado Salsa website shall emulate the clean, polished aesthetic of Brinvale.example.

```html
<!DOCTYPE html>
<html lang="en">
<head>
<meta charset="utf-8">
<title>Rio Dorado Salsa</title>
<link rel="stylesheet" href="https://fonts.googleapis.com/css2?family=Oswald:wght@400;500;600;700&family=Poppins:wght@400;500;600&display=swap">
<style>
:root{
  --red:#c8202b;
  --red-dark:#a3141e;
  --cream:#f7f0e4;
  --ink:#111;
  --green:#6a9f3c;
  --green-dark:#4f8530;
  --yellow:#f7c02a;
  --orange:#f2952a;
  --white:#fff;
}
*{margin:0;padding:0;box-sizing:border-box}
html,body{width:1200px;height:3722px;overflow:hidden}
body{position:relative;background:var(--cream);font-family:'Poppins',sans-serif;color:var(--ink)}
.abs{position:absolute}

/* header */
.site-header{position:absolute;left:0;top:0;width:1200px;height:128px;background:var(--white);border-top:4px solid var(--red)}
.call{position:absolute;left:127px;top:31px;font:500 17px/22px 'Oswald',sans-serif;display:flex;align-items:center;gap:6px}
.call span{color:var(--red)}
.nav a{position:absolute;top:84px;font:500 18px/24px 'Oswald',sans-serif;color:var(--ink);text-decoration:none;text-transform:uppercase}
.nav a.active::after{content:"";position:absolute;left:6px;right:6px;bottom:-8px;height:2px;background:var(--red);border-radius:2px}
.brand{position:absolute;font-family:'Oswald',sans-serif;font-weight:700;color:var(--red);white-space:nowrap;line-height:1}
.header-brand{left:0;width:1200px;top:22px;text-align:center;font-size:44px}
.header-icons{position:absolute;left:1008px;top:28px;display:flex;gap:18px}

/* hero */
.hero{position:absolute;left:0;top:128px;width:1200px;height:581px;background:linear-gradient(120deg,#b5141f 0%,#d2222c 45%,#c01a24 100%);overflow:hidden}
.hero-kicker{position:absolute;left:127px;top:128px;font:500 33px/40px 'Oswald',sans-serif;color:var(--white)}
.hero-title{position:absolute;left:125px;top:168px;font:700 66px/70px 'Oswald',sans-serif;color:var(--white)}
.btn-outline{position:absolute;left:128px;top:335px;width:151px;height:52px;border:3px solid var(--white);border-radius:14px 4px 14px 4px;color:var(--white);font:600 23px/46px 'Oswald',sans-serif;text-align:center}
.hero-jars{position:absolute;left:557px;top:118px;width:564px;height:412px;border-radius:40px 40px 60px 60px;background:linear-gradient(90deg,#e45a2a,#8fba3c 50%,#f2a534)}

/* featured */
.featured{position:absolute;left:0;top:709px;width:1200px;height:778px;background:linear-gradient(180deg,#fdfbf6 0%,#f3e7d3 100%)}
.ornament{position:absolute;left:520px;width:163px;height:56px;border-radius:28px}
.section-title{position:absolute;left:0;width:1200px;text-align:center;font-family:'Oswald',sans-serif;font-weight:700;text-transform:uppercase}
.rule{position:absolute;height:3px;background:var(--ink)}
.product-name{position:absolute;left:130px;top:276px;font:600 46px/56px 'Oswald',sans-serif;color:var(--red)}
.product-copy{position:absolute;left:126px;top:350px;width:430px;font-size:17.5px;line-height:30.5px;color:#333}
.btn-solid{position:absolute;background:var(--red);color:var(--white);border-radius:14px 4px 14px 4px;text-align:center;font-family:'Oswald',sans-serif;font-weight:600}
.feature-circle{position:absolute;left:682px;top:244px;width:388px;height:388px;border-radius:50%;background:radial-gradient(circle,#f9b04a 0%,#f08a22 60%,#e8701a 100%)}
.feature-jar{position:absolute;left:766px;top:290px;width:220px;height:336px;border-radius:30px 30px 40px 40px;background:linear-gradient(180deg,#d8b84a 0%,#d8b84a 14%,#e4541f 15%,#f5a531 60%,#c3351c 100%)}

/* reviews */
.reviews{position:absolute;left:0;top:1487px;width:1200px;height:650px;background:linear-gradient(160deg,#78ab43 0%,var(--green) 50%,var(--green-dark) 100%)}
.review-card{position:absolute;top:251px;width:252px;height:278px;background:var(--white);border-radius:6px;padding:32px 30px 0 36px}
.stars{display:block;height:14px}
.review-quote{margin-top:18px;font:600 15px/20px 'Poppins',sans-serif;color:var(--ink)}
.review-body{margin-top:4px;font-size:14.5px;line-height:20px;color:#444}
.review-name{position:absolute;left:36px;top:228px;font:500 14.5px/20px 'Poppins',sans-serif}
.arrow-btn{position:absolute;top:365px;width:42px;height:42px;border:2px solid var(--white);border-radius:50%;display:flex;align-items:center;justify-content:center}

/* recipes */
.recipes{position:absolute;left:0;top:2137px;width:1200px;height:748px;background:radial-gradient(ellipse at 50% 40%,#fcd63a 0%,var(--yellow) 55%,var(--orange) 100%)}
.recipe-photo{position:absolute;left:127px;top:203px;width:423px;height:425px;background:linear-gradient(135deg,#b9652a,#d8852f 45%,#8a3c1a);border:3px solid var(--white);outline:2px solid #5a3a1a;border-radius:14px}
.recipe-title{position:absolute;left:605px;top:224px;font:500 32px/40px 'Oswald',sans-serif;color:var(--ink)}
.recipe-copy{position:absolute;left:605px;top:290px;width:466px;font-size:16.3px;line-height:27.3px;color:#222}
.dots{position:absolute;left:622px;top:600px;display:flex;gap:9px}
.dots i{width:11px;height:11px;border-radius:50%;background:#caa03a;display:block}
.dots i.on{background:var(--ink)}

/* social band */
.social-band{position:absolute;left:0;top:2885px;width:1200px;height:198px;background:var(--red)}
.social-title{position:absolute;left:0;width:1200px;top:74px;text-align:center;font:500 40px/48px 'Oswald',sans-serif;color:var(--white)}
.social-rule{position:absolute;left:307px;top:129px;width:585px;height:3px;background:var(--white)}
.feed-photo{position:absolute;top:3102px;width:286px;height:279px}

/* footer */
.site-footer{position:absolute;left:0;top:3381px;width:1200px;height:341px;background:linear-gradient(180deg,#fbf7ef,#f3e9d8)}
.footer-email{position:absolute;left:188px;top:102px;font:500 15px/23px 'Oswald',sans-serif;text-transform:uppercase}
.footer-brand{left:0;width:1200px;top:98px;text-align:center;font-size:60px}
.footer-links a{position:absolute;font:500 16px/20px 'Oswald',sans-serif;color:var(--ink);text-decoration:none;text-transform:uppercase}
.copyright{position:absolute;left:0;width:1200px;top:244px;text-align:center;font-size:15.5px;line-height:26px;text-transform:uppercase}
</style>
</head>
<body>

<svg width="0" height="0" style="position:absolute"><defs><path id="st" d="M7 0l2 4.6 5 .4-3.8 3.3 1.2 4.9L7 10.6 2.6 13.2l1.2-4.9L0 5l5-.4z"/></defs></svg>

<header class="site-header">
  <div class="call">
    <svg width="18" height="18" viewBox="0 0 24 24" fill="none" stroke="#c8202b" stroke-width="2"><path d="M22 16.9v3a2 2 0 0 1-2.2 2 19.8 19.8 0 0 1-8.6-3.1 19.5 19.5 0 0 1-6-6A19.8 19.8 0 0 1 2.1 4.2 2 2 0 0 1 4.1 2h3a2 2 0 0 1 2 1.7c.1 1 .4 1.9.7 2.8a2 2 0 0 1-.5 2.1L8 9.9a16 16 0 0 0 6 6l1.3-1.3a2 2 0 0 1 2.1-.4c.9.3 1.8.6 2.8.7a2 2 0 0 1 1.7 2z"/></svg>
    <span>CALL:</span> 555 014 2736
  </div>
  <nav class="nav">
    <a class="active" href="#" style="left:126px">Home</a>
    <a href="#" style="left:210px">Product</a>
    <a href="#" style="left:318px">Where to Buy</a>
    <a href="#" style="left:736px">Recipe</a>
    <a href="#" style="left:827px">About</a>
    <a href="#" style="left:917px">Review</a>
    <a href="#" style="left:1011px">Contact</a>
  </nav>
  <div class="brand header-brand">Rio Dorado</div>
  <div class="header-icons">
    <svg width="24" height="24" viewBox="0 0 24 24" fill="none" stroke="#111" stroke-width="1.8"><circle cx="12" cy="8" r="4.5"/><path d="M3.5 22c0-4.7 3.8-8 8.5-8s8.5 3.3 8.5 8"/></svg>
    <svg width="24" height="24" viewBox="0 0 24 24" fill="none" stroke="#c8202b" stroke-width="1.8"><rect x="3.5" y="7" width="17" height="15" rx="1.5"/><path d="M8.5 10V5.5a3.5 3.5 0 0 1 7 0V10"/></svg>
  </div>
</header>

<section class="hero">
  <div class="hero-kicker">RIO DORADO</div>
  <h1 class="hero-title">SPICE UP<br>YOUR MEALS!</h1>
  <div class="btn-outline">SHOP NOW</div>
  <svg class="abs" style="left:0;top:0" width="1200" height="581" viewBox="0 0 1200 581">
    <path d="M419 581 C520 470 700 448 850 456 C1000 464 1120 500 1200 544 L1200 581 Z" fill="#fdfbf6"/>
  </svg>
  <div class="hero-jars" role="img" aria-label="Three jars of Rio Dorado salsa: habanero, verde and all natural"></div>
</section>

<section class="featured">
  <div class="ornament" style="top:43px;background:rgba(200,32,43,.18)" role="img" aria-label="Decorative red swirl ornament"></div>
  <h2 class="section-title" style="top:106px;font-size:55px;line-height:60px">Featured Product</h2>
  <div class="rule" style="left:434px;top:176px;width:332px"></div>
  <h3 class="product-name">ALL NATURAL SALSA</h3>
  <p class="product-copy">Lorem ipsum dolor sit amet, consectetur adipis cing elit, sed do eiusmod tempor incididunt ut labore et dolore magna aliqua. Quis ipsum suspe ndisse ultrices gravida. Risus commodo viverra maecenas accumsan</p>
  <div class="btn-solid" style="left:130px;top:521px;width:146px;height:49px;font-size:23px;line-height:49px">SHOP NOW</div>
  <div class="feature-circle" role="img" aria-label="Orange sunburst backdrop"></div>
  <div class="feature-jar" role="img" aria-label="Jar of Rio Dorado all natural salsa"></div>
</section>

<section class="reviews">
  <div class="ornament" style="top:92px;background:rgba(255,255,255,.3)" role="img" aria-label="Decorative white swirl ornament"></div>
  <h2 class="section-title" style="top:153px;font-size:35px;line-height:40px;font-weight:600;color:#fff">Reviews</h2>
  <div class="rule" style="left:541px;top:205px;width:117px;background:#fff"></div>

  <div class="arrow-btn" style="left:106px">
    <svg width="14" height="14" viewBox="0 0 14 14" fill="none" stroke="#fff" stroke-width="2"><path d="M9 2 4 7l5 5"/></svg>
  </div>
  <div class="arrow-btn" style="left:1049px">
    <svg width="14" height="14" viewBox="0 0 14 14" fill="none" stroke="#fff" stroke-width="2"><path d="M5 2l5 5-5 5"/></svg>
  </div>

  <article class="review-card" style="left:179px">
    <svg class="stars" width="72" height="14" viewBox="0 0 72 14" fill="#f0a030"><use href="#st"/><use href="#st" x="14.5"/><use href="#st" x="29"/><use href="#st" x="43.5"/><use href="#st" x="58"/></svg>
    <p class="review-quote">“Very good, and I’m a salsa snob!”</p>
    <p class="review-body">Lorem ipsum dolor lotsit amet, consectetur adipis cing elit, sed do eiusmod tempor incididunt ut lab ore et dolore maa.</p>
    <p class="review-name">-Dana Reyes</p>
  </article>
  <article class="review-card" style="left:474px">
    <svg class="stars" width="72" height="14" viewBox="0 0 72 14" fill="#f0a030"><use href="#st"/><use href="#st" x="14.5"/><use href="#st" x="29"/><use href="#st" x="43.5"/><use href="#st" x="58"/></svg>
    <p class="review-quote">“Awesome taste, fresh.”</p>
    <p class="review-body">Lorem ipsum dolor lotsit amet, consectetur adipis cing elit, sed do eiusmod tempor incididunt ut lab ore et dolore maa.</p>
    <p class="review-name">-Dana Reyes</p>
  </article>
  <article class="review-card" style="left:766px">
    <svg class="stars" width="72" height="14" viewBox="0 0 72 14" fill="#f0a030"><use href="#st"/><use href="#st" x="14.5"/><use href="#st" x="29"/><use href="#st" x="43.5"/><use href="#st" x="58"/></svg>
    <p class="review-quote">“Really good flavor.”</p>
    <p class="review-body">Lorem ipsum dolor lotsit amet, consectetur adipis cing elit, sed do eiusmod tempor incididunt ut lab ore et dolore maa.</p>
    <p class="review-name">-Dana Reyes</p>
  </article>
</section>

<section class="recipes">
  <h2 class="section-title" style="top:76px;font-size:60px;line-height:64px">Recipes</h2>
  <div class="rule" style="left:538px;top:149px;width:123px"></div>
  <div class="recipe-photo" role="img" aria-label="Spoonful of cheesy Mexican beef and rice"></div>
  <h3 class="recipe-title">ONE POT MEXICAN BEEF AND RICE</h3>
  <p class="recipe-copy">This One Pot Mexican Beef and Rice is the ultimate weeknight dinner—quick to prepare, easy to clean up, and packed with bold flavor in every bite. Ground beef is browned and simmered with beef broth, sweet corn, and Rio Dorado salsa, then combined with instant rice and melted cheddar for a hearty, satisfying meal that comes together in just 30 minutes.</p>
  <div class="btn-solid" style="left:605px;top:509px;width:163px;height:47px;font-size:21px;line-height:47px;font-weight:500">VIEW DETAILS</div>
  <div class="dots"><i class="on"></i><i></i><i></i><i></i></div>
</section>

<section class="social-band">
  <h2 class="social-title">FOLLOW RIODORADOSALSA’S ON SNAPGRID</h2>
  <div class="social-rule"></div>
</section>
<div class="feed-photo" style="left:0;width:276px;background:linear-gradient(135deg,#5a3a1e,#d08a2a 55%,#8a4a1a)" role="img" aria-label="Baked cheesy chicken topped with salsa and green onion"></div>
<div class="feed-photo" style="left:298px;background:radial-gradient(circle,#c2281a 0%,#a81c14 60%,#7a7a78 100%)" role="img" aria-label="Bowl of red salsa with fresh cilantro"></div>
<div class="feed-photo" style="left:606px;background:linear-gradient(160deg,#e8dcc0,#c89a5a 55%,#8a5a2a)" role="img" aria-label="Layered dip with cheese, sour cream and chips"></div>
<div class="feed-photo" style="left:914px;background:linear-gradient(135deg,#d8a060,#b0452a 55%,#7a2a18)" role="img" aria-label="Shredded meat taco with cilantro"></div>

<footer class="site-footer">
  <svg class="abs" style="left:127px;top:106px" width="48" height="36" viewBox="0 0 48 36" fill="none" stroke="#c8202b" stroke-width="3"><rect x="2" y="2" width="44" height="32" rx="2"/><path d="M2 4l22 17L46 4M2 34l16-15M46 34 30 19"/></svg>
  <div class="footer-email">Email address:<br>support@riodoradosalsa.example</div>
  <div class="brand footer-brand">Rio Dorado</div>
  <nav class="footer-links">
    <a href="#" style="left:859px;top:86px">Product</a>
    <a href="#" style="left:1003px;top:86px">About</a>
    <a href="#" style="left:859px;top:126px">Where to Buy</a>
    <a href="#" style="left:1003px;top:126px">Review</a>
    <a href="#" style="left:859px;top:166px">Recipe</a>
    <a href="#" style="left:1003px;top:166px">Contact</a>
  </nav>
  <p class="copyright">© 2025 © Rio Dorado Salsa.<br>All rights reserved. Privacy Policy</p>
</footer>

</body>
</html>
```